mortgage company professional business card

We would like to revamp our business card. Logos and current card attached.

Target Market(s)

white collar professionals

Industry/Entity Type

Mortgage Lender

Contact Information for Business Card

Looking for a sharp professional feel with white background for business card. No gloss. Looking for emboss.

Requirements
Must have
• -Professional touch
• -Emboss and raised lettering
• -Social media icons
• name, title, Phone, email, NMLS and web
• Complement logo and web

```html
<!DOCTYPE html>
<html lang="en">
<head>
<meta charset="utf-8">
<title>Harborline Lending – Business Card</title>
<link href="https://fonts.googleapis.com/css2?family=Oswald:wght@500&family=Roboto:wght@400;500;700&display=swap" rel="stylesheet">
<style>
  :root {
    --backdrop: #2a2a2c;
    --card-front: #f7f7f6;
    --card-back: #252527;
    --brand-navy: #26386f;
    --brand-green: #2ea44f;
    --name-blue: #2f4a8a;
    --text-light: #f2f2f2;
    --text-grey: #6b6b6b;
    --icon-blue: #3b5fa8;
    --divider: #8a8a8a;
    --social-1: #4a79c9;
    --social-2: #e2604a;
    --social-3: #2aa6dc;
    --social-4: #22b5e6;
  }
  * { margin: 0; padding: 0; box-sizing: border-box; }
  html, body { width: 1200px; height: 900px; overflow: hidden; background: var(--backdrop); }
  .stage { position: relative; width: 1200px; height: 900px; }
  .card {
    position: absolute; left: 240px; width: 720px; height: 411px;
    box-shadow: 0 10px 30px rgba(0,0,0,.45);
  }
  .card-front { top: 30px; background: var(--card-front); }
  .card-back { top: 459px; background: var(--card-back); }

  .brand { position: absolute; top: 125px; left: 0; width: 100%; text-align: center; }
  .brand-lockup { display: inline-block; text-align: right; }
  .brand-name {
    display: flex; align-items: center; gap: 14px;
    font-family: 'Roboto', sans-serif; font-weight: 700; font-size: 50px;
    color: var(--brand-navy); letter-spacing: -.5px; line-height: 1.1;
  }
  .brand-mark { width: 30px; height: 30px; background: var(--brand-green); }
  .tagline {
    margin-top: 2px; font-family: 'Roboto', sans-serif; font-weight: 500;
    font-size: 19px; color: var(--text-grey);
  }
  .front-url {
    position: absolute; top: 300px; width: 100%; text-align: center;
    font-family: 'Roboto', sans-serif; font-size: 17px; letter-spacing: 8px; color: var(--text-grey);
  }

  .social { position: absolute; top: 24px; right: 24px; display: flex; gap: 4px; }
  .social span { width: 26px; height: 26px; border-radius: 50%; }
  .social .s1 { background: var(--social-1); }
  .social .s2 { background: var(--social-2); }
  .social .s3 { background: var(--social-3); }
  .social .s4 { background: var(--social-4); }

  .identity { position: absolute; top: 116px; right: 400px; text-align: right; }
  .person-name {
    font-family: 'Oswald', sans-serif; font-weight: 500; font-size: 40px;
    color: var(--name-blue); letter-spacing: .5px; line-height: 1.05;
  }
  .person-title {
    font-family: 'Roboto', sans-serif; font-weight: 500;
    font-size: 17px; color: var(--brand-green);
  }
  .divider { position: absolute; left: 342px; top: 100px; width: 2px; height: 110px; background: linear-gradient(var(--divider), transparent); }

  .contacts { position: absolute; left: 370px; top: 98px; list-style: none; }
  .contacts li {
    display: flex; align-items: center; gap: 12px; height: 24px;
    font-family: 'Roboto', sans-serif; font-size: 18px; color: var(--text-light);
  }
  .contacts svg { width: 16px; height: 16px; fill: var(--icon-blue); flex: none; }

  .address {
    position: absolute; left: 40px; bottom: 60px; display: flex; align-items: center; gap: 6px;
    font-family: 'Roboto', sans-serif; font-size: 18px; color: var(--text-light);
  }
  .address svg { width: 16px; height: 20px; fill: var(--icon-blue); }
</style>
</head>
<body>
<main class="stage">
  <section class="card card-front">
    <div class="brand">
      <div class="brand-lockup">
        <div class="brand-name"><span class="brand-mark"></span>Harborline Lending</div>
        <p class="tagline">Here for every step.</p>
      </div>
    </div>
    <p class="front-url">www.harborline.com</p>
  </section>

  <section class="card card-back">
    <div class="social"><span class="s1"></span><span class="s2"></span><span class="s3"></span><span class="s4"></span></div>

    <div class="identity">
      <h1 class="person-name">DANIEL REYES</h1>
      <p class="person-title">CEO/FOUNDER</p>
    </div>
    <div class="divider"></div>

    <ul class="contacts">
      <li><svg viewBox="0 0 16 16"><path d="M3 1l3 3-2 2c1 2 3 4 5 5l2-2 3 3-2 3C6 15 1 10 0 3z"/></svg>555 214 7380</li>
      <li><svg viewBox="0 0 16 16"><path d="M4 0h8a1 1 0 011 1v14a1 1 0 01-1 1H4a1 1 0 01-1-1V1a1 1 0 011-1zm1 2v10h6V2z"/></svg>555 309 6127</li>
      <li><svg viewBox="0 0 16 16"><path d="M4 1h8v4H4zM1 6h14v7h-3v2H4v-2H1zm4 4v4h6v-4z"/></svg>555 782 4056</li>
      <li><svg viewBox="0 0 16 16"><path d="M1 3h14v10H1zm1 1l6 5 6-5z"/></svg>daniel@harborline.com</li>
      <li><svg viewBox="0 0 16 16"><circle cx="8" cy="8" r="7"/></svg>www.harborline.com</li>
    </ul>

    <p class="address"><svg viewBox="0 0 16 20"><path d="M8 0a7 7 0 017 7c0 5-7 13-7 13S1 12 1 7a7 7 0 017-7zm0 4a3 3 0 100 6 3 3 0 000-6z"/></svg>4210 Willow Bend Road, Juneau, Alaska 99801</p>
  </section>
</main>
</body>
</html>
```